Web Design Project

I have a website which looks dull and uninteresting. I'd like to apply a fresh and clean look to it, which better reflects the quality of the service I sell.The website address is http://www.brightquillpages.co.uk.

Target Market(s)

Financial advisers (financially sophisticated individuals)

Industry/Entity Type

It Service

Requirements
Should not have
• Please do not use obvious but irrelevant and boring imagery such as banks, pages from the MQ, money, books or libraries. Prefer slick relevant graphics and crisp typography.

```html
<!DOCTYPE html>
<html lang="en">
<head>
<meta charset="utf-8">
<title>BrightQuillPages – Sign up for a membership</title>
<link rel="stylesheet" href="https://fonts.googleapis.com/css2?family=Open+Sans:wght@400;600;700&display=swap">
<style>
  :root {
    --page-bg: #f6f6f6;
    --ink-strong: #474c52;
    --ink-body: #6f6f6f;
    --ink-soft: #8a8a8a;
    --rule: #dcdcdc;
    --brand-blue: #4a7fa6;
    --brand-blue-dark: #3a6a8d;
    --nav-bg: #e6e6e6;
    --nav-line: #c4c4c4;
    --bar-dark: #3e4246;
    --field-bg: #f1f1f1;
    --field-line: #cfcfcf;
    --accent-fill: #ececec;
    --footer-bg: #2d2e32;
    --footer-head: #e9e9e9;
    --footer-link: #6d6f73;
    --footer-badge: #242528;
  }
  * { box-sizing: border-box; margin: 0; padding: 0; }
  html, body { width: 953px; height: 1200px; overflow: hidden; }
  body {
    position: relative;
    background: var(--page-bg);
    font-family: "Open Sans", Arial, sans-serif;
    color: var(--ink-body);
  }
  a { color: inherit; text-decoration: none; }

  /* Header */
  .brand { position: absolute; left: 67px; top: 40px; display: flex; align-items: center; gap: 10px; }
  .brand-mark { width: 30px; height: 32px; background: var(--brand-blue); border-radius: 3px; }
  .brand-name { font-size: 26px; font-weight: 700; color: var(--ink-strong); letter-spacing: -0.5px; }

  .signup-btn {
    position: absolute; left: 385px; top: 36px; width: 79px; height: 36px;
    background: linear-gradient(var(--brand-blue), var(--brand-blue-dark));
    border-radius: 4px; color: #fff; font-size: 11px; font-weight: 600;
    display: flex; align-items: center; justify-content: center;
  }
  .main-nav {
    position: absolute; left: 475px; top: 36px; width: 410px; height: 36px;
    display: flex; background: linear-gradient(#f0f0f0, var(--nav-bg));
    border: 1px solid var(--nav-line); border-radius: 4px; overflow: hidden;
  }
  .main-nav a {
    display: flex; align-items: center; justify-content: center; gap: 6px;
    font-size: 10.5px; font-weight: 600; color: #333; border-left: 1px solid var(--nav-line);
    white-space: nowrap;
  }
  .main-nav a:first-child { border-left: 0; }
  .util-links {
    position: absolute; right: 72px; top: 92px; font-size: 10.5px; color: var(--ink-soft);
  }

  .rule { position: absolute; left: 67px; width: 818px; height: 1px; background: var(--rule); }

  .intro { position: absolute; left: 67px; top: 148px; width: 818px; text-align: center; }
  .intro h1 { font-size: 37px; font-weight: 700; color: var(--ink-strong); letter-spacing: -0.5px; line-height: 52px; }
  .intro p { margin-top: 8px; font-size: 14px; line-height: 22px; color: var(--ink-body); white-space: nowrap; }

  /* Membership section */
  .section-bar {
    position: absolute; left: 67px; top: 334px; width: 818px; height: 38px;
    background: var(--bar-dark); border-radius: 4px; color: #fff;
    font-size: 12px; font-weight: 700; padding-left: 30px; display: flex; align-items: center;
  }
  .signup-notes { position: absolute; left: 84px; top: 452px; font-size: 10.8px; line-height: 15px; color: #555; white-space: nowrap; }
  .signup-notes p + p { margin-top: 15px; }
  .accent-panel {
    position: absolute; left: 372px; top: 417px; width: 89px; height: 278px;
    background: linear-gradient(90deg, var(--accent-fill), var(--page-bg));
    border-radius: 6px;
  }

  .signup-form { position: absolute; left: 430px; top: 449px; width: 455px; }
  .form-row { display: flex; align-items: center; justify-content: flex-end; margin-bottom: 13px; }
  .form-row label { font-size: 10.5px; color: #444; margin-right: 14px; }
  .form-row .field { width: 249px; height: 29px; background: var(--field-bg); border: 1px solid var(--field-line); }
  .cost-row { display: flex; margin-top: 4px; font-size: 11px; font-weight: 700; color: #444; }
  .cost-row .cost-label { width: 192px; text-align: right; margin-right: 14px; }
  .terms-row { display: flex; margin-top: 13px; }
  .terms-row p { width: 192px; text-align: right; font-size: 10px; line-height: 12px; color: #444; white-space: nowrap; }
  .terms-row p a { text-decoration: underline; }
  .checkbox { width: 12px; height: 12px; margin-left: 14px; margin-top: 2px; border: 1px solid #999; background: #fff; }

  /* Footer */
  .site-footer { position: absolute; left: 5px; top: 789px; width: 948px; height: 411px; background: var(--footer-bg); }
  .footer-col { position: absolute; top: 46px; }
  .footer-col h3 { font-size: 11.5px; font-weight: 400; color: var(--footer-head); margin-bottom: 6px; }
  .footer-col a { display: block; font-size: 11.5px; line-height: 16.7px; color: var(--footer-link); }
  .footer-badge { position: absolute; left: 428px; top: 200px; width: 70px; height: 70px; border-radius: 50%; background: var(--footer-badge); }
  .copyright { position: absolute; left: 0; top: 280px; width: 926px; text-align: center; font-size: 10px; line-height: 16px; color: var(--footer-link); }
</style>
</head>
<body>

<header>
  <a class="brand" href="http://www.brightquillpages.co.uk">
    <span class="brand-mark"></span>
    <span class="brand-name">BrightQuillPages</span>
  </a>
  <a class="signup-btn" href="#">SIGN UP</a>
  <nav class="main-nav">
    <a href="#" style="width:63px" aria-label="Home">
      <svg width="14" height="13" viewBox="0 0 14 13"><path d="M7 0 L14 6 H12 V13 H8.5 V9 H5.5 V13 H2 V6 H0 Z" fill="#333"/></svg>
    </a>
    <a href="#" style="width:87px">New Page
      <svg width="7" height="5" viewBox="0 0 7 5"><path d="M0 0 H7 L3.5 5 Z" fill="#333"/></svg>
    </a>
    <a href="#" style="width:87px">A- Z Articles</a>
    <a href="#" style="width:99px">Enter the library</a>
    <a href="#" style="width:74px">Contact Us</a>
  </nav>
  <p class="util-links">Forgotten your password? | A comment to make? | A question to ask? | Want something writiten?</p>
</header>

<div class="rule" style="top:134px"></div>

<section class="intro">
  <h1>Use our articles copyright-free in perpetuity</h1>
  <p>One year's membership of the library costs £49 + VAT (£58.80). As a member, you can download as many of our<br>files and guides - including new articles and guides as they're added - whenever you want and<br>use them (with one exception) as you want.</p>
</section>

<div class="rule" style="top:297px"></div>

<main>
  <h2 class="section-bar">SIGN UP FOR A MEMBERSHIP</h2>

  <div class="signup-notes">
    <p>To set up your membership, please complete this<br>form and tick the terms and conditions box. You'll<br>then see confirmation of your details and the<br>'proceed' button. On receipt of your payment, we'll<br>e-mail your login details to you, which you will<br>need to enter (via the login section on our<br>home page) to gain access to the library.</p>
    <p>We use SwiftPay to process membership payments.<br>If you don't hold a SwiftPay account, please have<br>a credit or debit card to hand.</p>
    <p>Memberships are payable to 'Penwell Copy Ltd'.<br>SwiftPay will generate a printable receipt of your<br>payment</p>
  </div>

  <div class="accent-panel" role="img" aria-label="Large faint decorative bracket linking the notes to the form"></div>

  <form class="signup-form">
    <div class="form-row"><label>Your Name:</label><span class="field"></span></div>
    <div class="form-row"><label>Your Email-address:</label><span class="field"></span></div>
    <div class="form-row"><label>Your Choosen password:</label><span class="field"></span></div>
    <div class="cost-row"><span class="cost-label">Cost + VAT @ 20%:</span><span>£58.80</span></div>
    <div class="terms-row">
      <p>Please tick this box to confirm that<br>you have read our few and simple<br><a href="#">terms and conditions</a></p>
      <span class="checkbox"></span>
    </div>
  </form>
</main>

<footer class="site-footer">
  <div class="footer-col" style="left:70px">
    <h3>Quick Links</h3>
    <a href="#">Home</a><a href="#">Articles</a><a href="#">Support</a><a href="#">Contact</a><a href="#">Login</a>
  </div>
  <div class="footer-col" style="left:277px">
    <h3>Connect With Us</h3>
    <a href="#">Facenet</a><a href="#">Chirper</a>
  </div>
  <div class="footer-col" style="left:491px">
    <h3>Get in Touch</h3>
    <a href="#">Contact form</a><a href="#">Email</a>
  </div>
  <div class="footer-col" style="left:701px">
    <h3>Help</h3>
    <a href="#">Support</a><a href="#">FAQ</a><a href="#">Help</a>
  </div>
  <div class="footer-badge"></div>
  <p class="copyright">Copyright ©2011 &lt;Copyright Info&gt;<br>&lt;More copyright information&gt;. All rights reserved</p>
</footer>

</body>
</html>
```